Tall Reed Dairy Business cards

We need a logo design for our family dairy. Included on the cards should be my name/my husbands name/the dairy name/ all the phone numbers/address and email. The name is Tall Reed Dairy, LLC. We would like to use our farm mascot pic on the card. We know the pictures I sent you are of a beef cow but she is the mascot of the farm. We were thinking that maybe put a picture of her head in the middle of the card with a "B" on one side and a "D" on the other side with a "C" around the picture of the cow. But we are open to any ideas. We are looking for something kind of professional and a design that that can be used on cards, clothing and a car sign. Black lettering and blue for the other color...or what looks good.
Updates

Target Market(s)

All

Industry/Entity Type

Farming

Contact Information for Business Card

Marta Lusk Owner (555)210-4817
Doran Whitby Owner (555)473-9102
Tall Reed Dairy, LLC (555)586-2265
Tallreeddairy@examplemail.test
7162 County Lane 9, Kewaskum, WI 53040

Font styles to use
Sans Serif

Colors
3176b5
3c7bb8
3277b5
0255a3

Requirements
Must have
• Some design that incorporates a drawing/pic of the cow pictures that were sent.
Nice to have
• no suggestions
Should not have
• no suggestions

```html
<!DOCTYPE html>
<html lang="en">
<head>
<meta charset="utf-8">
<title>Tall Reed Dairy – Business Card</title>
<link rel="stylesheet" href="https://fonts.googleapis.com/css2?family=Montserrat:wght@400;700&display=swap">
<style>
  :root {
    --page-bg: #ececec;
    --card-bg: #f7f7f7;
    --brand-blue: #3f62ad;
    --brand-blue-light: #6284c6;
    --ink: #1c1c1c;
    --mascot-dark: #6b5a45;
    --mascot-light: #b8a98f;
  }
  * { margin: 0; padding: 0; box-sizing: border-box; }
  html, body {
    width: 1200px;
    height: 787px;
    overflow: hidden;
    background: var(--page-bg);
    font-family: "Montserrat", Arial, sans-serif;
  }
  .stage {
    width: 1200px;
    height: 787px;
    display: flex;
    align-items: center;
    justify-content: center;
  }
  .business-card {
    position: relative;
    width: 400px;
    height: 700px;
    background: var(--card-bg);
    box-shadow: 0 10px 30px rgba(0,0,0,0.12);
    display: flex;
    flex-direction: column;
  }
  .brand-band {
    height: 160px;
    background: var(--brand-blue);
    display: flex;
    align-items: center;
    justify-content: center;
    gap: 16px;
  }
  .mascot-portrait {
    width: 62px;
    height: 62px;
    border-radius: 50%;
    border: 3px solid #ffffff;
    background: radial-gradient(circle at 40% 45%, var(--mascot-light), var(--mascot-dark));
    flex-shrink: 0;
  }
  .brand-name {
    color: #ffffff;
    font-weight: 700;
    font-size: 30px;
    letter-spacing: 0.5px;
  }
  .contact-block {
    flex: 1;
    display: flex;
    flex-direction: column;
    align-items: center;
    justify-content: center;
    text-align: center;
    color: var(--ink);
    font-size: 18px;
    line-height: 1.3;
    gap: 26px;
    padding-bottom: 20px;
  }
  .person-name {
    color: var(--brand-blue);
    font-weight: 700;
    text-transform: uppercase;
    font-size: 20px;
  }
  .person-role { font-weight: 400; color: var(--ink); text-transform: none; }
  .company-name { font-weight: 700; font-size: 20px; }
  .postal { font-style: normal; }
  .footer-stripe {
    height: 32px;
    background: var(--brand-blue);
    border-top: 8px solid var(--brand-blue-light);
  }
</style>
</head>
<body>
<main class="stage">
  <article class="business-card">
    <header class="brand-band">
      <div class="mascot-portrait" role="img" aria-label="Portrait of the farm's cow mascot"></div>
      <span class="brand-name">Tall Reed Dairy</span>
    </header>
    <section class="contact-block">
      <div class="contact-person">
        <p class="person-name">Marta Lusk,<span class="person-role"> Owner</span></p>
        <p class="phone">(555)210-4817</p>
      </div>
      <div class="contact-person">
        <p class="person-name">Doran Whitby,<span class="person-role"> Owner</span></p>
        <p class="phone">(555)473-9102</p>
      </div>
      <div class="contact-company">
        <p class="company-name">Tall Reed Dairy, LLC</p>
        <p class="phone">(555)586-2265</p>
      </div>
      <p class="email">tallreeddairy@examplemail.test</p>
      <address class="postal">7162 County Lane 9,<br>Fernvale, WI 54999</address>
    </section>
    <footer class="footer-stripe"></footer>
  </article>
</main>
</body>
</html>
```